Needing a business Card for new fire company.

Dalvo, sales fire equipment and parts. We also do tree clearing for the forest service. My logo will be attached to this. I am also looking for a design that when people see the card it stick with them and they will remember my sales team giving it to them.

```html
<!DOCTYPE html>
<html lang="en">
<head>
<meta charset="utf-8">
<title>Dalvo Business Card</title>
<link href="https://fonts.googleapis.com/css2?family=Karla:wght@400;700&family=Roboto:wght@500&display=swap" rel="stylesheet">
<style>
  :root {
    --backdrop: #d9d2ca;
    --card-frost: #e4dfda;
    --card-edge: #bdb4ac;
    --ink-dark: #1f1f21;
    --fire-red: #8e1a1c;
    --fire-deep: #6b0b0e;
    --name-tint: #d8c6b9;
    --text-light: #f1e6de;
    --icon-bg: #f4f1ee;
  }
  html, body {
    margin: 0;
    padding: 0;
    width: 969px;
    height: 1200px;
    overflow: hidden;
    background: var(--backdrop);
  }
  .card {
    position: absolute;
    left: 237px;
    top: 167px;
    width: 494px;
    height: 866px;
    border-radius: 26px;
    overflow: hidden;
    background: linear-gradient(180deg, #ebe7e3 0%, var(--card-frost) 100%);
    box-shadow: 0 0 0 1.5px var(--card-edge), 0 18px 40px rgba(60, 40, 30, 0.18);
  }
  .brand-name {
    position: absolute;
    top: 122px;
    left: 0;
    width: 100%;
    text-align: center;
    font-family: "Karla", sans-serif;
    font-weight: 700;
    font-size: 84px;
    line-height: 88px;
    letter-spacing: 4px;
    color: var(--ink-dark);
  }
  .fire-field {
    position: absolute;
    left: 0;
    top: 300px;
    width: 100%;
    height: 566px;
    background: linear-gradient(180deg,
      rgba(142, 26, 28, 0) 0%,
      rgba(142, 26, 28, 0.35) 22%,
      var(--fire-deep) 42%,
      var(--fire-red) 75%,
      #911c1e 100%);
  }
  .contact-block {
    position: absolute;
    left: 0;
    top: 620px;
    width: 100%;
    text-align: center;
  }
  .person-name {
    margin: 0;
    font-family: "Roboto", sans-serif;
    font-weight: 500;
    font-size: 31px;
    line-height: 40px;
    color: var(--name-tint);
  }
  .person-role {
    margin: 0;
    font-family: "Karla", sans-serif;
    font-weight: 400;
    font-size: 18px;
    line-height: 24px;
    letter-spacing: 1px;
    color: var(--text-light);
  }
  .icon-row {
    display: flex;
    justify-content: center;
    gap: 4px;
    margin-top: 20px;
  }
  .icon-row svg {
    width: 30px;
    height: 30px;
  }
  .contact-lines {
    margin-top: 12px;
    font-family: "Karla", sans-serif;
    font-weight: 400;
    font-size: 20px;
    line-height: 28px;
    letter-spacing: 1px;
    color: var(--text-light);
  }
</style>
</head>
<body>
  <main class="card">
    <div class="brand-name">DALVO</div>
    <div class="fire-field" role="img" aria-label="Large red flame graphic rising from the lower edge of the card"></div>
    <section class="contact-block">
      <p class="person-name">DANIEL BROOKS</p>
      <p class="person-role">President</p>
      <div class="icon-row">
        <svg viewBox="0 0 30 30" aria-label="Phone">
          <circle cx="15" cy="15" r="14" fill="var(--icon-bg)" stroke="#2a2a2a" stroke-width="1.5"/>
          <path d="M10.5 8.5c1-.6 1.8-.4 2.3.5l1.1 2c.4.8.2 1.4-.5 1.9l-.8.5c.6 1.8 1.9 3.2 3.6 4l.5-.8c.5-.7 1.1-.9 1.9-.5l2 1.1c.9.5 1 1.3.5 2.3-.9 1.6-2.6 2.1-4.3 1.3-3.5-1.6-6-4.3-7.3-7.9-.6-1.6 0-3.3 1.3-4.4z" fill="#1f1f21"/>
        </svg>
        <svg viewBox="0 0 30 30" aria-label="Email">
          <circle cx="15" cy="15" r="14" fill="var(--icon-bg)" stroke="#2a2a2a" stroke-width="1.5"/>
          <rect x="8.5" y="10.5" width="13" height="9" rx="1" fill="#1f1f21"/>
          <path d="M8.8 11l6.2 4.6 6.2-4.6" fill="none" stroke="#f4f1ee" stroke-width="1.2"/>
        </svg>
        <svg viewBox="0 0 30 30" aria-label="Website">
          <circle cx="15" cy="15" r="14" fill="var(--icon-bg)" stroke="#2a2a2a" stroke-width="1.5"/>
          <circle cx="15" cy="15" r="7" fill="none" stroke="#1f1f21" stroke-width="1.6"/>
          <ellipse cx="15" cy="15" rx="3" ry="7" fill="none" stroke="#1f1f21" stroke-width="1.3"/>
          <line x1="8" y1="15" x2="22" y2="15" stroke="#1f1f21" stroke-width="1.3"/>
        </svg>
      </div>
      <div class="contact-lines">
        <div class="contact-phone">555-318-4720</div>
        <div class="contact-email">name@dalvo.com</div>
        <div class="contact-web">www.dalvo.com</div>
      </div>
    </section>
  </main>
</body>
</html>
```